Business Card - connecting 2 souls and beggining the journey of self discovery

Logo on the front
with tag line

On the back list of services and contact details

Seminars
workshops
Coaching
podcasts

Daniel Porthwick
Health & Wellbeing Life Coach
0491 372 815
daniel@wovenpathwellness.example
wovenpathwellness.example

Industry/Entity Type

Life Coaching

Contact Information for Business Card

I like the use of colour from the logo to be used. I'm not a fan of white.

Requirements
Must have
• My tagline: The journey home starts with you
Nice to have
• Use of colour that is in the mind body soul logo

```html
<!DOCTYPE html>
<html lang="en">
<head>
<meta charset="utf-8">
<title>Woven Path Wellness – Business Card</title>
<link rel="stylesheet" href="https://fonts.googleapis.com/css2?family=Source+Sans+3:wght@400;500;600&display=swap">
<style>
  :root {
    --backdrop: #e9e6e3;
    --card-tint-start: #f6ecf7;
    --card-tint-mid: #fdf0e6;
    --card-tint-end: #eaf6f1;
    --card-dark: #2a2a2a;
    --ink: #111111;
    --rule: #8c8c8c;
    --brand-grey: #8e8e8e;
    --brand-dot: #f08a3c;
    --tagline: #c9c9c9;
    --shadow: rgba(0, 0, 0, 0.18);
  }
  * { box-sizing: border-box; margin: 0; padding: 0; }
  html, body {
    width: 1200px;
    height: 900px;
    overflow: hidden;
    background: var(--backdrop);
    font-family: "Source Sans 3", "Myriad Pro", sans-serif;
    color: var(--ink);
  }
  .canvas {
    position: relative;
    width: 1200px;
    height: 900px;
  }
  .card {
    position: absolute;
    border-radius: 16px;
    box-shadow: 0 10px 28px var(--shadow);
  }
  /* Contact side */
  .card--contact {
    left: 78px;
    top: 35px;
    width: 588px;
    height: 363px;
    background: linear-gradient(120deg, var(--card-tint-start) 0%, var(--card-tint-mid) 55%, var(--card-tint-end) 100%);
    text-align: center;
  }
  .contact__name {
    position: absolute;
    left: 0; right: 0;
    top: 66px;
    font-size: 23px;
    font-weight: 600;
    letter-spacing: 0.1px;
  }
  .contact__role {
    position: absolute;
    left: 0; right: 0;
    top: 99px;
    font-size: 16.5px;
    font-weight: 400;
  }
  .contact__rule {
    position: absolute;
    left: 194px;
    top: 140px;
    width: 199px;
    height: 0;
    border-top: 1.5px solid var(--rule);
  }
  .contact__details {
    position: absolute;
    left: 0; right: 0;
    top: 166px;
    list-style: none;
    font-size: 16.5px;
    line-height: 24px;
  }
  .contact__services {
    position: absolute;
    left: 0; right: 0;
    top: 270px;
    display: flex;
    justify-content: center;
    align-items: center;
    list-style: none;
    font-size: 16.5px;
    font-weight: 600;
  }
  .contact__services li + li::before {
    content: "";
    display: inline-block;
    width: 8px;
    height: 8px;
    margin: 0 14px 2px;
    border-radius: 50%;
    background: var(--ink);
    vertical-align: middle;
  }
  /* Brand side */
  .card--brand {
    left: 390px;
    top: 507px;
    width: 564px;
    height: 348px;
    background: var(--card-dark);
  }
  .brand__dot {
    position: absolute;
    left: 222px;
    top: 84px;
    width: 122px;
    height: 122px;
    border-radius: 50%;
    background: var(--brand-dot);
  }
  .brand__name {
    position: absolute;
    left: 0; right: 0;
    top: 230px;
    text-align: center;
    font-size: 33px;
    font-weight: 500;
    letter-spacing: -0.8px;
    color: var(--brand-grey);
  }
  .brand__tagline {
    position: absolute;
    left: 0; right: 0;
    top: 284px;
    text-align: center;
    font-size: 15px;
    font-weight: 400;
    letter-spacing: 0.4px;
    color: var(--tagline);
  }
</style>
</head>
<body>
<main class="canvas">
  <section class="card card--contact">
    <h1 class="contact__name">Daniel Porthwick</h1>
    <p class="contact__role">Health &amp; Wellbeing Life Coach</p>
    <div class="contact__rule"></div>
    <ul class="contact__details">
      <li>0491 372 815</li>
      <li>daniel@wovenpathwellness.example</li>
      <li>www.wovenpathwellness.example</li>
    </ul>
    <ul class="contact__services">
      <li>Seminars</li>
      <li>Workshops</li>
      <li>Coaching</li>
      <li>Podcasts</li>
    </ul>
  </section>

  <section class="card card--brand">
    <div class="brand__dot"></div>
    <p class="brand__name">Woven Path Wellness</p>
    <p class="brand__tagline">The journey home starts with you</p>
  </section>
</main>
</body>
</html>
```